Consulting company needs Business Cards - rough concept provided

I'm looking for someone to take our business card idea and make is slick and polished - to communicate our high-end, sophisticated, serious consulting business. We have a rough layout we did in-house. We are open to ideas on repo-ing elements, adjusting sizes, typefaces etc... within the general concept we've already come up with. We want it to be super-clean and sophisticated. We want to keep the white backgrounds, and blue brand colors. Our goal is to print with painted blue edges on thick cardstock. Thank you!!

```html
<!DOCTYPE html>
<html lang="en">
<head>
<meta charset="utf-8">
<title>Tallharbor Business Card</title>
<link rel="stylesheet" href="https://fonts.googleapis.com/css2?family=Lato:wght@300;400;700&display=swap">
<style>
  :root {
    --backdrop: #f0f0f0;
    --card: #ffffff;
    --brand-blue: #0a97dc;
    --sky-blue: #b7e2f5;
    --soft-grey: #b9b9b9;
    --ink: #111111;
  }
  * { margin: 0; padding: 0; box-sizing: border-box; }
  html, body { width: 1200px; height: 1000px; overflow: hidden; }
  body {
    position: relative;
    background: var(--backdrop);
    font-family: 'Lato', sans-serif;
    color: var(--ink);
  }
  .card {
    position: absolute;
    left: 248px;
    width: 704px;
    height: 405px;
    background: var(--card);
    border-radius: 18px;
    border-left: 2px solid var(--brand-blue);
    border-bottom: 3px solid var(--brand-blue);
    overflow: hidden;
  }
  .card--front { top: 77px; }
  .card--back { top: 522px; }

  .wordmark {
    position: absolute;
    left: 52px;
    top: 58px;
    font-size: 47px;
    font-weight: 700;
    letter-spacing: 1px;
    line-height: 1;
    color: var(--brand-blue);
  }
  .flight-illustration {
    position: absolute;
    left: 384px;
    top: 18px;
    width: 292px;
    height: 200px;
    border-radius: 12px;
    background: linear-gradient(135deg, #ffffff 0%, var(--sky-blue) 100%);
  }
  .holder { position: absolute; left: 52px; top: 204px; }
  .holder-name {
    font-size: 26px;
    font-weight: 700;
    font-variant: small-caps;
    letter-spacing: 0.5px;
    line-height: 1;
  }
  .holder-role { font-size: 16px; margin-top: 3px; }

  .contact {
    position: absolute;
    right: 65px;
    top: 250px;
    list-style: none;
    text-align: right;
    font-size: 15px;
    line-height: 22.6px;
  }
  .contact li { position: relative; }
  .contact-icon {
    position: absolute;
    right: -18px;
    top: 6px;
    width: 11px;
    height: 11px;
    fill: var(--ink);
  }
  .statement { display: block; }
  .statement text { font-family: 'Lato', sans-serif; }
  .accent { fill: var(--brand-blue); font-weight: 400; }
  .placeholder { fill: var(--soft-grey); font-weight: 300; }
  .headline { fill: var(--brand-blue); font-weight: 300; }
</style>
</head>
<body>

<section class="card card--front">
  <div class="wordmark">TALLHARBOR</div>
  <div class="flight-illustration" role="img" aria-label="Light blue paper plane illustration with a looping dashed flight path"></div>

  <div class="holder">
    <div class="holder-name">Dana Whitfield</div>
    <div class="holder-role">Brand Consultant</div>
  </div>

  <ul class="contact">
    <li>(555) 014 2290
      <svg class="contact-icon" viewBox="0 0 12 12"><path d="M2.5 0.5 L4.5 0.5 L5.3 3.2 L3.9 4.3 C4.6 5.9 6 7.3 7.7 8.1 L8.8 6.7 L11.5 7.5 L11.5 9.5 C11.5 10.6 10.6 11.5 9.5 11.5 C4.5 11.3 0.7 7.5 0.5 2.5 C0.5 1.4 1.4 0.5 2.5 0.5 Z"/></svg>
    </li>
    <li>dana@tallharbor.com
      <svg class="contact-icon" viewBox="0 0 12 12"><path d="M0.5 2.5 H11.5 V10 H0.5 Z M0.5 2.5 L6 6.5 L11.5 2.5" fill="#111" stroke="#fff" stroke-width="0.8"/></svg>
    </li>
    <li>tallharbor.com
      <svg class="contact-icon" viewBox="0 0 12 12"><circle cx="6" cy="6" r="5.5"/><path d="M3 3 C5 4 4 6 6 7 C7 8 6 10 7 11 M8 2 C9 3 10 4 11 5" fill="none" stroke="#fff" stroke-width="1"/></svg>
    </li>
    <li>4820 Meridian Ave, Ste 210
      <svg class="contact-icon" viewBox="0 0 12 12"><path d="M6 0.5 C8.5 0.5 10 2.3 10 4.4 C10 7 6 11.5 6 11.5 C6 11.5 2 7 2 4.4 C2 2.3 3.5 0.5 6 0.5 Z M6 3 A1.5 1.5 0 1 0 6 6 A1.5 1.5 0 1 0 6 3 Z" fill-rule="evenodd"/></svg>
    </li>
    <li>Brookfield, CA 90210</li>
  </ul>
</section>

<section class="card card--back">
  <svg class="statement" width="704" height="405" viewBox="0 0 704 405">
    <text x="44" y="75" font-size="34" textLength="611" lengthAdjust="spacing"><tspan class="accent">WE HELP </tspan><tspan class="placeholder">[TARGET DEMOGRAPHIC]</tspan></text>
    <text x="44" y="114" font-size="26" textLength="611" lengthAdjust="spacing"><tspan class="accent">ACHIEVE </tspan><tspan class="placeholder">[DESIRED EMOTIONAL OUTCOME] </tspan><tspan class="accent">BY</tspan></text>
    <text class="placeholder" x="44" y="173" font-size="54" textLength="613" lengthAdjust="spacing">[OUR UNIQUE APPROACH]</text>
    <text class="headline" x="38" y="290" font-size="133" textLength="620" lengthAdjust="spacing">BECAUSE</text>
    <text class="placeholder" x="44" y="353" font-size="58" textLength="613" lengthAdjust="spacing">[OUR BRAND BELIEFS]</text>
  </svg>
</section>

</body>
</html>
```